Gold Crest Pickleball Tournament

Design a poster for the Maplewood Vista Series, a pickleball tournament series. Each event will have it's own poster with a different design. The posters should be different but related graphically. The first assignment is Posters 1 and 2. The posters should be bold, exciting, fun and show movement. The attached files are for content, hierarchy for text but not design. Logo typeface: Legend 54. Logo blue: cmyk blue: 2b3990 R: 43 G:57 B:144
Please contact me with questions.

```html
<!DOCTYPE html>
<html lang="en">
<head>
<meta charset="utf-8">
<title>Gold Crest Pickleball Tournament – Maplewood Vista Series</title>
<link rel="stylesheet" href="https://fonts.googleapis.com/css2?family=Barlow+Condensed:ital,wght@0,500;0,600;0,700;1,700&display=swap">
<style>
  :root {
    --navy: #111a4d;
    --blue: #2b3990;
    --blue-deep: #1b2470;
    --yellow: #ffd22e;
    --yellow-light: #ffe85a;
    --red: #d8232a;
    --white: #ffffff;
    --board: #3a3a3c;
  }
  * { margin: 0; padding: 0; box-sizing: border-box; }
  html, body { width: 1200px; height: 860px; overflow: hidden; background: var(--board); }
  body { font-family: "Barlow Condensed", "Arial Narrow", sans-serif; }
  .poster {
    position: absolute; left: 0; top: 30px; width: 1200px; height: 800px;
    overflow: hidden;
    background: linear-gradient(160deg, #1c2a6e 0%, var(--navy) 45%, #202f86 100%);
  }
  .shapes { position: absolute; inset: 0; }
  .sanction {
    position: absolute; left: 70px; top: 53px;
    color: var(--white); font-style: italic; font-weight: 700; font-size: 44px; line-height: 1;
  }
  .title {
    position: absolute; left: 68px; top: 110px;
    font-weight: 700; font-size: 66px; line-height: 1; white-space: nowrap;
    background: linear-gradient(180deg, var(--yellow-light), #f6b416);
    -webkit-background-clip: text; background-clip: text; color: transparent;
  }
  .events {
    position: absolute; left: 52px; top: 191px;
    display: grid; grid-template-columns: 240px 280px; row-gap: 22px;
  }
  .event-name { color: var(--white); font-weight: 700; font-size: 35px; line-height: 1; white-space: nowrap; }
  .event-name::before { content: "»"; color: #9aa0c4; font-size: 28px; margin-right: 4px; }
  .event-date { color: var(--yellow); font-weight: 500; font-size: 21px; line-height: 1.1; margin-left: 20px; margin-top: 5px; white-space: nowrap; }
  .features { position: absolute; left: 74px; top: 372px; list-style: none; }
  .features li { color: var(--navy); font-weight: 700; font-size: 26px; line-height: 32px; white-space: nowrap; }
  .features li::before { content: "»"; color: #8a7a2a; margin-right: 6px; }
  .sponsor { position: absolute; left: 70px; top: 488px; color: var(--yellow); font-weight: 700; line-height: 1; white-space: nowrap; }
  .sponsor .big { font-size: 48px; }
  .sponsor .small { font-size: 35px; margin-top: 0; }
  .contact { position: absolute; left: 70px; top: 580px; font-size: 22px; line-height: 27px; color: var(--white); font-weight: 600; white-space: nowrap; }
  .contact .label { font-style: italic; font-weight: 700; }
  .contact .link { color: var(--yellow); }
  .contact .venue { margin-top: 10px; font-weight: 500; line-height: 31px; }
  .series-name {
    position: absolute; left: 855px; top: 672px; width: 320px; text-align: center;
    font-weight: 700; line-height: 1; white-space: nowrap;
  }
  .series-name .main { color: var(--white); font-size: 42px; }
  .series-name .sub { color: var(--yellow); font-size: 36px; margin-top: 2px; letter-spacing: 1px; }
</style>
</head>
<body>
<main class="poster">
  <svg class="shapes" width="1200" height="800" viewBox="0 0 1200 800">
    <defs>
      <linearGradient id="photoTone" x1="0" y1="0" x2="1" y2="1">
        <stop offset="0" stop-color="#d9d9d9"/>
        <stop offset="0.45" stop-color="#7d7f86"/>
        <stop offset="1" stop-color="#3f4148"/>
      </linearGradient>
      <linearGradient id="redWash" x1="1" y1="0" x2="0" y2="1">
        <stop offset="0" stop-color="#e3242b"/>
        <stop offset="1" stop-color="#7a1620"/>
      </linearGradient>
    </defs>
    <polygon points="894,0 1177,0 673,800 388,800" fill="url(#photoTone)" role="img" aria-label="Photo of a pickleball player lunging to hit a yellow ball"/>
    <polygon points="1100,0 1177,0 673,800 560,800" fill="url(#redWash)" opacity="0.75"/>
    <polygon points="1177,0 1200,0 1200,800 673,800" fill="var(--blue)"/>
    <polygon points="1200,330 1200,800 980,800" fill="var(--blue-deep)" opacity="0.6"/>
    <line x1="894" y1="0" x2="388" y2="800" stroke="var(--white)" stroke-width="6"/>
    <line x1="1177" y1="0" x2="673" y2="800" stroke="var(--white)" stroke-width="6"/>
    <polygon points="0,364 490,364 440,475 0,475" fill="var(--yellow)"/>
    <rect x="988" y="390" width="212" height="121" fill="var(--white)"/>
    <circle cx="1094" cy="450" r="36" fill="var(--blue)"/>
    <circle cx="1015" cy="606" r="50" fill="var(--yellow)"/>
  </svg>

  <p class="sanction">MVPA SANCTIONED</p>
  <h1 class="title">Pickleball Tournaments</h1>

  <section class="events">
    <div><p class="event-name">GOLD CREST</p><p class="event-date">November 6-7, 2021</p></div>
    <div><p class="event-name">RALLY AND SLAM</p><p class="event-date">September 18-19, 2021</p></div>
    <div><p class="event-name">HARBOR SLAM</p><p class="event-date">February 20-21, 2021</p></div>
    <div><p class="event-name">SUMMIT SLAM</p><p class="event-date">December 4-5, 2021</p></div>
  </section>

  <ul class="features">
    <li>WOMEN'S, MEN'S AND MIXED DOUBLES</li>
    <li>ZEPHYR GLIDE YELLOW INDOOR BALL</li>
    <li>CASH PRIZES!</li>
  </ul>

  <section class="sponsor">
    <p class="big">SPONSORSHIP</p>
    <p class="small">OPPORTUNITIES AVAILABLE</p>
  </section>

  <section class="contact">
    <p class="label">QUESTIONS:</p>
    <p class="link">http://maplewoodvistaseries@example.com</p>
    <p class="label">REGISTRATION:</p>
    <p class="link">http://courtbracketsonline.example/</p>
    <p class="venue">Harborview Sportsplex<br>218 Orchard Ave, Millbrook, MA</p>
  </section>

  <div class="series-name">
    <p class="main">MAPLEWOOD VISTA</p>
    <p class="sub">– SERIES –</p>
  </div>
</main>
</body>
</html>
```